Stationary Set and Logo Update **PAYMENT GUARANTEED**

Stationery Design and Logo Update

About Us

Trindex Supply is a wholesale distributor of OEM [original brand] and compatible [generic brand] parts and supplies for use in copiers, faxes, printers, and multi-function machines. In plain English…we sell all the parts and supplies [such as toner] that make up any office equipment which outputs an image on paper.

Trindex was the 1st distributor to develop and sell a generic brand copier part in the United States. We have been in business since 1972 [nearly 40 years]. Our tagline is "The Steady Choice," as in our company was the first alternative product that copier dealers had to buying original brand copier parts. Trindex is known for offering reliable and cost-effective OEM and compatible products.

Project

We require a fresh, modern and corporate identity. Please submit a stationary package inclusive of a double-sided business card (2" x 3.5"), letterhead (8.5'x11"), and standard #10 envelope (4-1/8” x 9-1/2). You may use our current logo or preferably your take on an updated one. If an attempt is made in updating the logo #004D8E or a similar hue should be used as the primary color.

The design should be clean, simple, modern and professional and make an immediate impact.

Target Market(s)

Copier and printer dealers who lease and service imaging equipment in the United States and Latin America.

Industry/Entity Type

Business

Requirements
Must have
• Simple, clean, modern and professional. Please use #004D8E or a similar hue as the primary color. Letterhead must accommate (2) addresses. We have 2 locations.
Nice to have
• A simple, modern update to our current logo. https://assets.mailvorbo.example/fs030/5520384417702/img/418.jpg
Should not have
• More than (2) colors on logo.

```html
<!DOCTYPE html>
<html lang="en">
<head>
<meta charset="utf-8">
<title>Trindex Supply Stationery</title>
<link href="https://fonts.googleapis.com/css2?family=Arimo:wght@400;700&display=swap" rel="stylesheet">
<style>
:root{
  --brand:#0a5aa8;
  --ink:#333;
  --line:#c9c9c9;
  --navy:#2b2a7d;
  --blue:#1e8fd6;
  --sky:#7cc7ec;
  --yellow:#ffe600;
  --gold:#f6b800;
  --orange:#ef7d1a;
  --red:#e1261c;
  --magenta:#d6137a;
  --pink:#f39ac0;
  --peach:#f6c2a8;
  --panel-blue:#1a86d0;
  --panel-orange:#e8771e;
  --tab-sky:#5fb8e8;
  --tab-pink:#ec5a9a;
  --tab-gold:#f7a81b;
}
*{margin:0;padding:0;box-sizing:border-box}
html,body{width:1200px;height:900px;overflow:hidden;background:#fff}
body{position:relative;font-family:'Arimo',Arial,sans-serif;color:var(--ink)}
.piece{position:absolute;background:#fff;border:1px solid var(--line)}
.logo{position:absolute;display:flex;align-items:center;gap:5px;color:var(--brand);font-weight:700}
.logo .dot{border-radius:50%;background:var(--brand)}
.color-strip{position:absolute;display:flex}
.color-strip span{flex:1}
.c1{background:var(--navy)}.c2{background:var(--blue)}.c3{background:var(--sky)}.c4{background:var(--yellow)}.c5{background:var(--gold)}
.c6{background:var(--orange)}.c7{background:var(--red)}.c8{background:var(--magenta)}.c9{background:var(--pink)}.c10{background:var(--peach)}

.envelope-front{left:56px;top:50px;width:444px;height:186px}
.envelope-front .logo{left:20px;top:22px;font-size:20px}
.envelope-front .logo .dot{width:12px;height:12px}
.return-address{position:absolute;left:22px;top:56px;font-size:5.5px;line-height:7px}
.return-address b{display:block;margin-top:4px}
.return-address b:first-child{margin-top:0}
.envelope-front .color-strip{left:4px;right:4px;top:172px;height:10px}

.envelope-back{left:56px;top:256px;width:444px;height:188px}
.envelope-flap{position:absolute;left:4px;top:4px;width:44px;height:178px;border:1px solid var(--line);border-radius:12px 0 0 12px}

.card{position:absolute;width:206px;height:360px;border:1px solid var(--line);border-radius:10px;overflow:hidden}
.card-front{left:56px;top:504px;background:linear-gradient(#f3f3f3,#d9d9d9)}
.card-front .logo{left:44px;top:68px;font-size:22px}
.card-front .logo .dot{width:13px;height:13px}
.card-bars{position:absolute;left:60px;top:146px;bottom:0;display:flex}
.card-bars span{width:28px}
.card-back{left:274px;top:504px;background:linear-gradient(#f6f6f6,#dcdcdc)}
.holder{position:absolute;top:28px;width:100%;text-align:center}
.holder-name{font-size:14px;font-weight:700;color:var(--panel-blue)}
.holder-title{font-size:10px;color:var(--panel-blue);margin-top:6px}
.tab{position:absolute;height:16px;font-size:8px;font-weight:700;color:#fff;display:flex;align-items:center;justify-content:center}
.tab-office{left:4px;top:174px;width:90px;background:var(--tab-sky)}
.tab-products{left:98px;top:174px;width:104px;background:var(--tab-pink)}
.tab-west{left:0;top:272px;width:96px;background:var(--tab-gold)}
.panel{position:absolute;left:0;right:0;color:#fff;text-align:center;font-size:8.5px;line-height:12px}
.panel-office{top:190px;height:82px;background:var(--panel-blue);padding-top:8px}
.panel-west{top:288px;bottom:0;background:var(--panel-orange);padding-top:8px}

.letterhead{left:552px;top:66px;width:604px;height:824px}
.letterhead .logo{left:24px;top:26px;font-size:24px}
.letterhead .logo .dot{width:14px;height:14px}
.letterhead-header{position:absolute;top:26px;display:flex;font-size:6.5px;line-height:8px}
.lh-office{left:196px}
.lh-west{left:390px}
.lh-address{text-align:right;padding-right:5px;border-right:1px solid #888}
.lh-phones{padding-left:5px}
.letterhead .color-strip{left:100px;top:746px;width:488px;height:20px}
</style>
</head>
<body>

<section class="piece envelope-front" aria-label="Envelope front">
  <div class="logo"><span class="dot"></span>Trindex</div>
  <div class="return-address">
    <b>Trindex Supply</b>Corporate Office<br>2280 SW 52nd Avenue<br>Harbor Point, FL 33312<br>Tel 800.555.0142
    <b>Trindex West</b>Calder Industrial Park #4<br>1745 Calder Way<br>Sparks Valley, NV 89530<br>Tel 775.555.0121
  </div>
  <div class="color-strip"><span class="c1"></span><span class="c2"></span><span class="c3"></span><span class="c4"></span><span class="c5"></span><span class="c6"></span><span class="c7"></span><span class="c8"></span><span class="c9"></span><span class="c10"></span></div>
</section>

<section class="piece envelope-back" aria-label="Envelope back">
  <div class="envelope-flap"></div>
</section>

<section class="card card-front" aria-label="Business card front">
  <div class="logo"><span class="dot"></span>Trindex</div>
  <div class="card-bars"><span class="c1"></span><span class="c8"></span><span class="c4"></span></div>
</section>

<section class="card card-back" aria-label="Business card back">
  <div class="holder">
    <div class="holder-name">Marisol Vetrano</div>
    <div class="holder-title">Marketing Coordinator</div>
  </div>
  <div class="tab tab-office">Corporate Office</div>
  <div class="tab tab-products">Trindex Supply</div>
  <div class="panel panel-office">2280 SW 52nd Avenue<br>Harbor Point, FL 33312<br>Toll Free: 800.555.0142<br>Direct: 954.555.0187<br>Email: mvetrano@trindex.com</div>
  <div class="tab tab-west">Trindex West</div>
  <div class="panel panel-west">West Coast Fulfillment Center<br>Calder Industrial Park #4<br>1745 Calder Way<br>Sparks Valley, NV 89530</div>
</section>

<section class="piece letterhead" aria-label="Letterhead">
  <div class="logo"><span class="dot"></span>Trindex</div>
  <div class="letterhead-header lh-office">
    <div class="lh-address"><b>TRINDEX SUPPLY</b><br>Corporate Office<br>2280 SW 52nd Avenue<br>Harbor Point, FL 33312</div>
    <div class="lh-phones"><br>Toll Free: 800.555.0142<br>Local: 954.555.0187<br>Fax: 954.555.0163</div>
  </div>
  <div class="letterhead-header lh-west">
    <div class="lh-address"><b>Trindex West</b><br>West Coast Fulfillment Center<br>Calder Industrial Park #4<br>1745 Calder Way, Sparks Valley, NV 89530</div>
    <div class="lh-phones"><br>Toll Free: 800.555.0142<br>Tel: 775.555.0121</div>
  </div>
  <div class="color-strip"><span class="c1"></span><span class="c2"></span><span class="c3"></span><span class="c4"></span><span class="c5"></span><span class="c6"></span><span class="c7"></span><span class="c8"></span><span class="c9"></span><span class="c10"></span></div>
</section>

</body>
</html>
```